Brevard médico-conseils - word template

We are dooing lot of médical report from word document. We dont print the text on a stationnary. We are producting the report and save it in pdf. So I need à word template. I want something more than just hard the logo. I would like the look of a stationnary in the word template.

I put an exemple of report. But the final don't have to look that way. Propose something more acurate.
After that I will need a business card.

Industry/Entity Type

Medical

Requirements
Must have
• We have to do a design that integrate are logo and color. You have the file in the project.
• The wrihting beteen the title must be in times new roman.
Nice to have
• We have 2 offices:
• Québec (Building Val-Doré) 512, ave des Tilleuls, local 210, G2K 4P7 T.418 555-7142 T.418 555-7189
• St-Romuald (Building Carrefour Marbel-Les quais) 2350, boul. des Érables, local 305, G7B 2N4. T.418 555-0263 F.418 555-0398
• Mail: info@BrevardMC.com and expertise@BrevardMC.com
• Web: www.BrevardMC.com
• For now you can type www.PTRV.ca to acces the web site.
Should not have
• The same look that the exemple. Because I want to upgrade the look of the company.

```html
<!DOCTYPE html>
<html lang="fr">
<head>
<meta charset="utf-8">
<title>Brevard médico-conseils – Rapport complémentaire du médecin</title>
<link href="https://fonts.googleapis.com/css2?family=Tinos:ital,wght@0,400;0,700;1,400;1,700&display=swap" rel="stylesheet">
<style>
  :root {
    --brand-blue: #2a6fc1;
    --brand-navy: #1d4f8c;
    --brand-orange: #f2a12a;
    --tint: #eef4fb;
    --ink: #1a1a1a;
    --muted: #4a5a70;
    --paper: #ffffff;
  }
  html, body { margin: 0; padding: 0; overflow: hidden; background: var(--paper); }
  .page {
    position: relative; width: 853px; height: 1200px; overflow: hidden;
    background: var(--paper); font-family: "Tinos", "Times New Roman", serif; color: var(--ink);
  }
  .edge-strip { position: absolute; top: 0; left: 0; width: 12px; height: 1140px; background: var(--brand-blue); }
  .edge-strip::after { content: ""; position: absolute; top: 0; left: 0; width: 12px; height: 120px; background: var(--brand-orange); }

  .masthead {
    position: absolute; top: 0; left: 12px; right: 0; height: 120px;
    display: flex; align-items: center; justify-content: space-between;
    padding: 0 48px 0 60px; box-sizing: border-box;
    border-bottom: 1px solid #d6e2f1;
  }
  .brand { display: flex; align-items: center; gap: 14px; }
  .brand-mark { width: 34px; height: 34px; border-radius: 50%; background: var(--brand-orange); }
  .brand-name { font-size: 36px; font-weight: 700; color: var(--brand-blue); }

  .doc-title {
    position: absolute; top: 146px; left: 72px; right: 48px; margin: 0;
    font-size: 20px; font-weight: 700; letter-spacing: 2px; color: var(--brand-navy);
    padding: 10px 0 10px 18px; background: var(--tint); border-left: 5px solid var(--brand-orange);
  }

  .section-head {
    position: absolute; left: 72px; right: 48px; margin: 0;
    display: flex; align-items: center; gap: 14px;
    font-size: 20px; font-weight: 700; letter-spacing: 3px; color: var(--brand-blue);
  }
  .section-head::after { content: ""; flex: 1; height: 2px; background: var(--brand-blue); opacity: 0.35; }

  .field { position: absolute; left: 90px; margin: 0; font-size: 15px; font-weight: 700; color: var(--ink); }
  .field .colon { position: absolute; left: 190px; color: var(--brand-blue); }
  .date-label { position: absolute; top: 1003px; left: 583px; font-size: 15px; font-weight: 700; }

  .note {
    position: absolute; top: 832px; left: 72px; right: 48px; margin: 0; text-align: center;
    font-size: 17px; font-style: italic; font-weight: 700; color: var(--brand-blue);
  }

  .offices {
    position: absolute; top: 1036px; left: 12px; right: 0; height: 104px;
    border-top: 3px solid var(--brand-orange);
    display: flex; justify-content: space-between; padding: 10px 48px 0 60px; box-sizing: border-box;
  }
  .office { font-style: normal; font-size: 12px; line-height: 18px; color: var(--muted); }
  .office h3 { margin: 0 0 2px; font-size: 13px; letter-spacing: 2px; color: var(--brand-navy); }
  .office-right { text-align: right; }

  .contact-band {
    position: absolute; left: 0; bottom: 0; width: 100%; height: 60px; background: var(--brand-navy);
    color: #fff; font-size: 13px; text-align: center;
    display: flex; flex-direction: column; justify-content: center; line-height: 20px;
  }
  .contact-band b { color: var(--brand-orange); }
</style>
</head>
<body>
<div class="page">
  <div class="edge-strip"></div>

  <header class="masthead">
    <div class="brand">
      <span class="brand-mark"></span>
      <span class="brand-name">Brevard médico-conseils</span>
    </div>
  </header>

  <h1 class="doc-title">RAPPORT COMPLÉMENTAIRE DU MÉDECIN</h1>

  <h2 class="section-head" style="top:210px">INFORMATION</h2>
  <p class="field" style="top:250px">NO. DE DOSSIER<span class="colon">:</span></p>
  <p class="field" style="top:274px">EMPLOYEUR<span class="colon">:</span></p>
  <p class="field" style="top:298px">EMPLOYÉ(E)<span class="colon">:</span></p>
  <p class="field" style="top:340px">POSTE<span class="colon">:</span></p>
  <p class="field" style="top:364px">DATE DE L'EXAMEN<span class="colon">:</span></p>

  <h2 class="section-head" style="top:412px">MÉDICAL</h2>
  <p class="field" style="top:452px">ANTÉCÉDENTS<span class="colon">:</span></p>
  <p class="field" style="top:637px">EXAMEN PHYSIQUE<span class="colon">:</span></p>
  <p class="field" style="top:688px">RECOMMANDATIONS<span class="colon">:</span></p>
  <p class="field" style="top:777px">DOSSIER DE CRTQ<span class="colon">:</span></p>

  <p class="note">(Pour la description exacte - voir le rapport de radiologie)</p>

  <p class="field" style="top:896px">RX-LOMBAIRE<span class="colon">:</span></p>
  <p class="field" style="top:958px">MÉDECIN<span class="colon">:</span></p>
  <p class="field" style="top:981px">RÉDACTION<span class="colon">:</span></p>
  <p class="field" style="top:1003px">VALIDATION<span class="colon">:</span></p>
  <div class="date-label">DATE:</div>

  <div class="offices">
    <address class="office office-left">
      <h3>QUÉBEC</h3>
      Building Val-Doré<br>
      512, ave des Tilleuls, local 210, G2K 4P7<br>
      T. 418 555-7142 &nbsp; T. 418 555-7189
    </address>
    <address class="office office-right">
      <h3>ST-ROMUALD</h3>
      Building Carrefour Marbel-Les quais<br>
      2350, boul. des Érables, local 305, G7B 2N4<br>
      T. 418 555-0263 &nbsp; F. 418 555-0398
    </address>
  </div>

  <footer class="contact-band">
    <span><b>Mail</b> info@BrevardMC.com &nbsp;·&nbsp; expertise@BrevardMC.com</span>
    <span><b>Web</b> www.BrevardMC.com &nbsp;·&nbsp; www.PTRV.ca to access the web site</span>
  </footer>
</div>
</body>
</html>
```